Coldforge Prime manufacturing Project

We are looking at getting a brand new design for a new company that deals in selling stainless tubing and other stainless still products such as handrails, Spigots, Balustrade Fittings
Glass, Glass fittings and Aluminium Channels

We require a very clean website that deals with the following colours:

Blue to light blues
Blacks
Greys to light Greys
Whites

We are open for other ideas BUT we *DO NOT* want any pinks, greens or bright colours except for backgrounds colours we have chosen above. (It can be solid, gradient or a subtle pattern)

YOU MUST KEEP THE LOGO AS IS. PLEASE DO NOT ALTER THE LOGO IN *ANY WAY* and the logo MUST be the same colours and fonts.

Logo is attached.

The site must contain these aspects:
jQuery Slider (Image slide show)
Top drop down Menus
Be no more than 900px wide
Text is to be to the w3C standards. (no special fonts)

We will chop up the design into html format. You just need to provide the PSD file.

The clients opposition is:
www.quorvatrim.example

Industry/Entity Type

It Company

Requirements
Nice to have
• Alter the logo in anyway

Files

```html
<!DOCTYPE html>
<html lang="en">
<head>
<meta charset="utf-8">
<title>Coldforge Prime Manufacturing</title>
<link rel="stylesheet" href="https://fonts.googleapis.com/css2?family=Open+Sans:wght@400;600&display=swap">
<style>
:root{
  --brand:#5a6a9a;
  --nav-top:#7b8bb8;
  --nav-bottom:#5d6d9c;
  --caption:#6f7fae;
  --tile-label:#3f5080;
  --footer:#3f5080;
  --dark-bar:#231f20;
  --heading:#555a60;
  --body-text:#5a5a5a;
  --call:#6477aa;
  --white:#ffffff;
  --frame:#e2e2e2;
}
*{margin:0;padding:0;box-sizing:border-box}
html,body{width:1200px;height:1100px;overflow:hidden;background:var(--white);font-family:"Open Sans",Arial,sans-serif}
.page{position:relative;width:1200px;height:1100px}
.top-rule{position:absolute;left:0;top:0;width:1200px;height:6px;background:var(--brand)}
.brand{position:absolute;left:150px;top:12px;width:170px;text-align:center}
.brand-mark{display:block;width:90px;height:90px;margin:0 0 0 32px;border-radius:50%;background:var(--brand)}
.brand-name{display:block;margin-top:4px;font-size:17px;font-weight:600;color:var(--brand);white-space:nowrap}
.contact{position:absolute;right:152px;top:56px;text-align:right}
.contact .call{font-size:15px;font-weight:600;color:var(--call)}
.contact .email{margin-top:5px;font-size:13px;color:#555}
.main-nav{position:absolute;left:150px;top:144px;width:900px;height:43px;background:linear-gradient(var(--nav-top),var(--nav-bottom))}
.main-nav ul{list-style:none;display:flex;height:43px;align-items:center}
.main-nav li{font-size:15px;font-weight:600;color:var(--white);position:absolute;top:12px}
.search{position:absolute;left:669px;top:5px;width:226px;height:32px;background:var(--white);border-radius:3px}
.search svg{position:absolute;right:8px;top:8px}
.search .divider{position:absolute;right:32px;top:4px;width:1px;height:24px;background:#ddd}
.slider{position:absolute;left:150px;top:195px;width:900px;height:341px;border:1px solid var(--frame);padding:3px}
.slide-photo{width:892px;height:333px;background:linear-gradient(100deg,#8a8784 0%,#b8b4ae 30%,#6f6b67 55%,#a09c97 80%,#7d7a76 100%)}
.caption{position:absolute;left:563px;top:48px;width:309px;height:226px;background:var(--caption);color:var(--white);padding:18px 17px}
.caption h2{font-size:18px;font-weight:400;line-height:24px;text-align:justify;letter-spacing:.5px}
.caption p{margin-top:8px;font-size:15px;line-height:21.5px;text-align:justify}
.dots{position:absolute;left:814px;top:306px;display:flex;gap:8px}
.dots span{width:12px;height:12px;background:var(--white);border:3px solid #222}
.dots span.active{border-color:var(--white);background:var(--caption)}
.section-bar{position:absolute;left:150px;top:548px;width:900px;height:34px;background:var(--dark-bar);color:var(--white);font-size:16px;padding:7px 10px}
.section-bar svg{position:absolute;right:10px;top:11px}
.products{position:absolute;left:150px;top:597px;width:900px;display:flex;justify-content:space-between}
.product{width:220px;height:164px}
.product .photo{height:125px}
.product .label{height:39px;background:var(--tile-label);color:var(--white);font-size:14px;font-weight:600;padding:11px 11px}
.welcome{position:absolute;left:150px;top:786px;width:600px}
.services{position:absolute;left:779px;top:786px;width:271px}
h3{font-size:18px;font-weight:400;color:var(--heading);height:47px}
.welcome .photo{position:absolute;left:0;top:47px;width:239px;height:204px;background:linear-gradient(90deg,#7f7a72,#c8ccd0 40%,#e4e6e8)}
.copy{font-size:11.3px;line-height:17px;color:var(--body-text);text-align:justify;height:206px;overflow:hidden}
.copy p+p{margin-top:17px}
.welcome .copy{margin-left:251px;width:349px}
.footer{position:absolute;left:0;top:1054px;width:1200px;height:46px;background:var(--footer)}
.footer .legal{position:absolute;left:149px;top:14px;font-family:Arial,sans-serif;font-size:12px;color:var(--white)}
.social{position:absolute;left:925px;top:9px;display:flex;gap:8px}
.social span{width:25px;height:26px;background:#1d1d1d}
</style>
</head>
<body>
<div class="page">
  <div class="top-rule"></div>
  <header>
    <div class="brand"><span class="brand-mark"></span><span class="brand-name">Coldforge Prime</span></div>
    <div class="contact">
      <div class="call">CALL US : (000) 000 0000</div>
      <div class="email">Email: info@coldforgeprime.example</div>
    </div>
    <nav class="main-nav">
      <ul>
        <li style="left:27px">HOME</li>
        <li style="left:138px">ABOUT US</li>
        <li style="left:278px">PRODUCTS</li>
        <li style="left:422px">SERVICES</li>
        <li style="left:555px">CONTACT</li>
      </ul>
      <div class="search">
        <span class="divider"></span>
        <svg width="16" height="16" viewBox="0 0 16 16"><circle cx="6" cy="6" r="4" fill="none" stroke="#999" stroke-width="2"/><line x1="9" y1="9" x2="14" y2="14" stroke="#999" stroke-width="2.5"/></svg>
      </div>
    </nav>
  </header>

  <section class="slider">
    <div class="slide-photo" role="img" aria-label="Close-up of a brushed stainless steel square handle"></div>
    <div class="caption">
      <h2>SED UT PERSPICIATIS UNDE OMNIS ISTE NATUS ERROR SIT VOLUPTATEM</h2>
      <p>accusantium doloremque laudan-tium, totam rem aperiam, eaque ipsa quae ab illo inventore veritatis et quasi architecto beatae vitae dicta sunt explicabo.</p>
    </div>
    <div class="dots"><span class="active"></span><span></span><span></span></div>
  </section>

  <div class="section-bar">PRODUCTS
    <svg width="22" height="10" viewBox="0 0 22 10"><polygon points="0,5 8,0 8,10" fill="#fff"/><polygon points="22,5 14,0 14,10" fill="#fff"/></svg>
  </div>
  <div class="products">
    <div class="product"><div class="photo" role="img" aria-label="Stainless handrail with wall bracket" style="background:linear-gradient(135deg,#bdbbb8,#7c7a78 60%,#a9a7a4)"></div><div class="label">HANDRAILS</div></div>
    <div class="product"><div class="photo" role="img" aria-label="Black plastic spigot on grey surface" style="background:linear-gradient(135deg,#b3b1ad,#9d9b98 50%,#bab8b4)"></div><div class="label">SPIGOTS</div></div>
    <div class="product"><div class="photo" role="img" aria-label="Chrome balustrade fitting on wooden rail" style="background:linear-gradient(135deg,#5a3a2a,#8a6a58 50%,#4a3024)"></div><div class="label">BALUSTRADE FITTINGS</div></div>
    <div class="product"><div class="photo" role="img" aria-label="Stacked aluminium channel profiles" style="background:linear-gradient(90deg,#cfd3d4,#a9adae 50%,#8f9495)"></div><div class="label">ALUMINIUM CHANNELS</div></div>
  </div>

  <section class="welcome">
    <h3>WELCOME TO COLDFORGE PRIME !</h3>
    <div class="photo" role="img" aria-label="Hand resting on a brushed steel rail"></div>
    <div class="copy">
      <p>Sed ut perspiciatis unde omnis iste natus error sit voluptatem accusantium doloremque laudantium, totam rem aperiam, eaque ipsa quae ab illo inventore veritatis et quasi architecto beatae vitae dicta sunt explicabo.</p>
      <p>Nemo enim ipsam voluptatem quia voluptas sit aspernatur aut odit aut fugit, sed quia consequuntur magni dolores eos qui ratione voluptatem sequi nesciunt. Neque porro quisquam est, qui dolorem ipsum quia dolor sit amet, consectetur, adipisci velit, sed quia non numquam eius modi tempora incidunt ut labore et dolore magnam aliquam quaerat voluptatem. Ut enim ad minima veniam, quis nostrum exercitationem ullam corporis suscipit laboriosam, nisi ut aliquid ex ea commodi.</p>
    </div>
  </section>

  <section class="services">
    <h3>OUR SERVICES</h3>
    <div class="copy">
      <p>Sed ut perspiciatis unde omnis iste natus error sit voluptatem accusantium doloremque laudantium, totam rem aperiam, eaque ipsa quae ab illo inventore veritatis et quasi architecto beatae vitae dicta sunt explicabo.</p>
      <p>Nemo enim ipsam voluptatem quia voluptas sit aspernatur aut odit aut fugit, sed quia consequuntur magni dolores eos qui ratione voluptatem sequi nesciunt. Neque porro quisquam est, qui dolorem ipsum quia dolor sit amet, consectetur, adipisci velit, sed quia non numquam eius modi tempora incidunt ut labore et dolore magnam.</p>
    </div>
  </section>

  <footer class="footer">
    <div class="legal">Copyright © 2013 Coldforge Prime. All rights reserved.</div>
    <div class="social"><span></span><span></span><span></span><span></span></div>
  </footer>
</div>
</body>
</html>
```